Nutrition Supplement Label for Zuno Brand

Natural health supplement company looking for a label design that can define brand. Bold, Clean, Crisp. Product is Apple Cider Vinegar Gummies. Bottle will be clear with Black top. Label size is 2.5 x6. Previous label was 2x8 which you'll see in files as example of label. colors suggested are white, red, black, green, gold. All colors don't need to used, just suggestions. Apple images, icons welcomed. Will send examples of working design as requested. In progress design below
Updates

Want more designs submitted. Of the 30, at least 25 designs submitted by 1 designers.

Target Market(s)

21-55 Women 60% Men 40%, Health Conscious Consumers.

Industry/Entity Type

Health and Wellness

Font styles to use
Serif
Sans Serif

Colors
00AB8E
00BBA5
67D7C9
C6EFE9
E9F9F6
59FF00
82FF00
B8FF75
E3FFCB
F4FFEA
FFC000
F8CF3A
FAE287
FDF2CF
FEFAEE
EE7325
F08F49
F5BC92
FAE3D3
FDF4ED
EB3D1F
EC4F4E
F09395
F8D3D4
FCEDEE

Requirements
Must have
• BQX PRODUCT CLAIMS: All product claims (for example, "Lose Weight...") need to have this symbol † after them which references the "These statements have not been evaluated by the BQX..." disclaimer. This is a requirement by the BQX. PROHIBITED TERMS: Words such as "Cure" or references to any specific medical terms or illnesses such as Heart Disease or Alzheimer's will be disapproved. Instead use more general terms such as "Supports Your Cardiovascular Health" or "Can Improve Memory Loss". Products can not be labelled Organic, but they can be called "Natural". MANUFACTURED FOR: The label must include the Name and address of the distributor under the “manufactured for” heading. It must also include the Street address if the firm name and address are not listed in a current city directory or telephone book, as well as the City or Town, State, and ZIP code. Label size is 2.5x6. Please include all designs on clear bottle black top mockup so that we can accurately see how label will look on product.
Nice to have
• Colors are suggested but not set in stone. Label base color can be white, black or red. Have fun with it.
Should not have
• No character or hard to read fonts.

```html
<!DOCTYPE html>
<html lang="en">
<head>
<meta charset="utf-8">
<title>Orvana Apple Cider Vinegar Gummies – Label</title>
<link rel="stylesheet" href="https://fonts.googleapis.com/css2?family=Montserrat:wght@400;500;600;700;800;900&display=swap">
<style>
  :root {
    --bg: #d1d1d3;
    --white: #ffffff;
    --red: #c8171e;
    --red-dark: #a81419;
    --badge-red: #e31b23;
    --silver-1: #c9c9c9;
    --silver-2: #f2f2f2;
    --ink: #1a1a1a;
    --ink-soft: #333333;
    --rule: #000000;
  }
  * { margin: 0; padding: 0; box-sizing: border-box; }
  html, body { width: 1200px; height: 2439px; overflow: hidden; }
  body { background: var(--bg); font-family: "Montserrat", sans-serif; color: var(--ink); position: relative; }

  .label {
    position: absolute; left: 10px; top: 970px;
    width: 1232px; height: 523px;
    transform: scale(0.9578); transform-origin: top left;
    background: var(--white); overflow: hidden;
  }
  .band-red {
    position: absolute; left: 0; top: 0; width: 1232px; height: 298px;
    background: linear-gradient(90deg, var(--red) 0%, var(--red-dark) 45%, var(--red) 100%);
  }
  .band-silver {
    position: absolute; left: 0; top: 0; width: 672px; height: 108px;
    background: linear-gradient(90deg, var(--silver-1), var(--silver-2) 30%, var(--silver-1) 60%, var(--silver-2) 90%);
    border-bottom-right-radius: 40px;
  }

  /* Left info panel */
  .info-panel {
    position: absolute; left: 30px; top: 33px; width: 362px; height: 470px;
    background: var(--white); border-radius: 6px;
    padding: 20px 14px 0 14px;
    font-size: 14.2px; line-height: 17.5px; font-weight: 500; text-align: justify;
  }
  .info-panel p { margin-bottom: 17px; }
  .info-panel .left { text-align: left; }

  /* Front panel */
  .brand {
    position: absolute; left: 437px; top: 50px;
    display: flex; align-items: center; gap: 8px;
    font-size: 40px; font-weight: 500; color: var(--ink-soft); letter-spacing: 0.5px;
  }
  .brand-dot { width: 14px; height: 14px; border-radius: 50%; background: #3f8f3a; }
  .title { position: absolute; left: 437px; color: var(--white); font-weight: 800; line-height: 1; }
  .title-top { top: 129px; font-size: 47px; }
  .title-main { top: 177px; font-size: 69px; letter-spacing: -0.5px; }
  .title-bottom { top: 240px; font-size: 47px; }

  .count-badge {
    position: absolute; left: 690px; top: 244px; width: 88px; height: 88px; border-radius: 50%;
    background: var(--badge-red); color: var(--white); text-align: center;
  }
  .count-badge .num { display: block; font-size: 40px; font-weight: 700; line-height: 1; margin-top: 13px; }
  .count-badge .unit { display: block; font-size: 12px; font-weight: 600; margin-top: 3px; }

  .claim { position: absolute; left: 439px; display: flex; align-items: center; gap: 16px; }
  .claim svg { width: 40px; height: 44px; }
  .claim span { font-size: 16.5px; font-weight: 700; line-height: 21px; }
  .claim-immune { top: 334px; }
  .claim-weight { top: 391px; }

  .apple-art {
    position: absolute; left: 652px; top: 338px; width: 140px; height: 150px;
    border-radius: 50% 50% 45% 45%;
    background: radial-gradient(circle at 60% 40%, #e53234, #b3202a 70%);
  }
  .dietary { position: absolute; left: 438px; top: 478px; font-size: 15px; font-weight: 700; }

  /* Supplement facts */
  .facts {
    position: absolute; left: 840px; top: 33px; width: 364px; height: 365px;
    background: var(--white); border: 2px solid var(--rule); padding: 4px 8px;
    font-size: 12.5px; line-height: 1.2;
  }
  .facts h2 { font-size: 31px; font-weight: 900; line-height: 1.05; letter-spacing: -0.3px; }
  .facts .serving { font-size: 11.5px; border-bottom: 7px solid var(--rule); padding-bottom: 3px; }
  .facts .row { display: flex; justify-content: space-between; border-bottom: 1px solid var(--rule); padding: 1px 0; }
  .facts .row .amt { display: flex; gap: 12px; }
  .facts .row .dv { width: 36px; text-align: right; }
  .facts .head { font-weight: 700; border-bottom: 4px solid var(--rule); padding-top: 4px; }
  .facts .sub { padding-left: 28px; }
  .facts .note { font-size: 9px; font-style: italic; display: block; }
  .facts .thick { border-bottom: 4px solid var(--rule); }
  .facts .footnote { font-size: 12px; line-height: 1.2; padding-top: 3px; }
  .other { position: absolute; left: 848px; top: 402px; width: 352px; font-size: 12px; line-height: 13.5px; }
  .distributor { position: absolute; left: 848px; top: 461px; width: 352px; font-size: 10.5px; line-height: 13px; text-align: center; }
</style>
</head>
<body>
  <div class="label">
    <div class="band-red"></div>
    <div class="band-silver"></div>

    <div class="info-panel">
      <p>SUGGESTED USE: As a dietary supplement, take two (2) Gummies once a day.</p>
      <p>CAUTION: Do not exceed recommended dose. Pregnant or nursing mothers, children under the age of 18, and individuals with a known medical condition should consult a physician before using this or any dietary supplement.</p>
      <p>KEEP OUT OF REACH OF CHILDREN. DO NOT USE IF SAFETY SEAL IS DAMAGED OR MISSING. STORE IN A COOL, DRY PLACE.</p>
      <p>*These statements have not been evaluated by the BQX. This product is not intended to diagnose, treat, cure or prevent any disease.</p>
      <p class="left">Lot # and Expiration Date Printed on bottom of Bottle<br>V2R0 SKU: XXXXX-840</p>
    </div>

    <div class="brand">Orvana<span class="brand-dot"></span></div>
    <div class="title title-top">APPLE CIDER</div>
    <div class="title title-main">VINEGAR</div>
    <div class="title title-bottom">GUMMIES</div>

    <div class="count-badge"><span class="num">60</span><span class="unit">GUMMIES</span></div>

    <div class="claim claim-immune">
      <svg viewBox="0 0 40 44" fill="none" stroke="#1a1a1a" stroke-width="3">
        <path d="M20 3 L36 9 V22 C36 32 29 38 20 41 C11 38 4 32 4 22 V9 Z"/>
        <circle cx="20" cy="22" r="9"/>
        <path d="M20 17 V27 M15 22 H25"/>
      </svg>
      <span>IMMUNE<br>SUPPORT</span>
    </div>
    <div class="claim claim-weight">
      <svg viewBox="0 0 40 44" fill="none" stroke="#1a1a1a" stroke-width="2.5">
        <ellipse cx="20" cy="14" rx="17" ry="10"/>
        <ellipse cx="20" cy="12" rx="6" ry="4"/>
        <path d="M3 14 V22 C3 28 12 30 20 40 C28 30 37 28 37 22 V14"/>
      </svg>
      <span>WEIGHT<br>SUPPORT</span>
    </div>

    <div class="apple-art" role="img" aria-label="Illustration of a red apple with a leaf and a cut slice"></div>
    <div class="dietary">DIETARY SUPPLEMENT</div>

    <div class="facts">
      <h2>Supplement Facts</h2>
      <div class="serving"><b>Serving Size:</b> 2 Pieces &nbsp;&nbsp;<b>Servings Per Container:</b> 30</div>
      <div class="row head"><span>Amount Per Serving</span><span>%DV</span></div>
      <div class="row"><span>Calories: 24</span><span>Calories from fat: 0</span></div>
      <div class="row"><span>Total Carbohydrates</span><span class="amt"><span>6g</span><span class="dv">2%</span></span></div>
      <div class="row"><span>Sodium <small>(as Sodium citrate)</small></span><span class="amt"><span>12mg</span><span class="dv">&lt;1%</span></span></div>
      <div class="row"><span>Sugar</span><span class="amt"><span>4g</span><span class="dv">**</span></span></div>
      <div class="row sub"><span>Includes Added Sugars</span><span class="amt"><span>4g</span><span class="dv">8%</span></span></div>
      <div class="row"><span>Folate</span><span class="amt"><span>400mcg DFE<span class="note">(240 mcg folic acid)</span></span><span class="dv">100%</span></span></div>
      <div class="row"><span>Vitamin B12 <small>(as Cyanocobalamin)</small></span><span class="amt"><span>2mcg</span><span class="dv">83%</span></span></div>
      <div class="row"><span>Apple Cider Vinegar Powder<span class="note">(Malus pumila mill)(Fruit)</span></span><span class="amt"><span>1000mg</span><span class="dv">**</span></span></div>
      <div class="row"><span>Pomegranate Juice Powder<span class="note">(Punica granatum L.)(Fruit)</span></span><span class="amt"><span>80mcg</span><span class="dv">**</span></span></div>
      <div class="row thick"><span>Beet Juice Powder <i>(Beta vulgaris L)(root)</i></span><span class="amt"><span>80mcg</span><span class="dv">**</span></span></div>
      <div class="footnote">† Percent Daily Value is based on a 2,000 calorie diet<br>** Daily Value (DV) not established</div>
    </div>
    <div class="other"><b>Other Ingredients:</b> Glucose Syrup, Sugar, Glucose, Pectin, Citric Acid, Natural Apple Flavour, Vegetable Oil (Contains Carnauba Wax), Purple Carrot Juice Concentrate, B-Carotene.</div>
    <div class="distributor"><b>Distributed By:</b> Company Name<br>Street Address | City, ST Zip Code | Website or Phone Number</div>
  </div>
</body>
</html>
```